Simple elegant business card

General card for a fin and television director.
Just want name, email, phone and address.

Target Market(s)

Prospective employers

Industry/Entity Type

Business

Requirements
Must have
• As above
Nice to have
• Logo but not necessary.
Should not have
• Not too colourful or funky.
• Simplicity and elegance the way to go.

```html
<!DOCTYPE html>
<html lang="en">
<head>
<meta charset="utf-8">
<title>Nora Hale — Business Card</title>
<link href="https://fonts.googleapis.com/css2?family=Jost:wght@400;500&display=swap" rel="stylesheet">
<style>
  :root {
    --backdrop: #e9e7e4;
    --card-front: #ffffff;
    --card-back: #1c1c1e;
    --ink: #161616;
    --ink-soft: #7a7a7a;
    --label: #b4b4b4;
    --back-name: #8a8a8c;
    --shadow: rgba(0, 0, 0, 0.18);
  }
  * { margin: 0; padding: 0; box-sizing: border-box; }
  html, body {
    width: 1200px;
    height: 888px;
    overflow: hidden;
    background: var(--backdrop);
    font-family: "Jost", "Futura", sans-serif;
  }
  .sheet {
    width: 1200px;
    height: 888px;
    display: flex;
    align-items: center;
    justify-content: center;
    gap: 60px;
  }
  .card {
    width: 525px;
    height: 300px;
    position: relative;
    box-shadow: 0 10px 28px var(--shadow);
  }
  .card--front { background: var(--card-front); }
  .card--back { background: var(--card-back); }

  .name {
    position: absolute;
    right: 40px;
    font-weight: 400;
    letter-spacing: 0.16em;
    text-transform: uppercase;
    white-space: nowrap;
  }
  .card--front .name {
    top: 132px;
    font-size: 31px;
    color: var(--ink);
  }
  .name__last { color: var(--ink-soft); }
  .card--back .name {
    top: 132px;
    font-size: 31px;
    color: var(--back-name);
  }
  .card--back .name__last { color: var(--back-name); }

  .contact {
    position: absolute;
    right: 40px;
    top: 186px;
    display: grid;
    grid-template-columns: auto auto;
    column-gap: 10px;
    font-size: 14px;
    line-height: 18px;
    letter-spacing: 0.03em;
  }
  .contact__label {
    color: var(--label);
    text-align: right;
  }
  .contact__value {
    color: var(--ink);
    text-align: right;
  }
</style>
</head>
<body>
  <main class="sheet">
    <section class="card card--front" aria-label="Business card front">
      <h1 class="name">Nora <span class="name__last">Hale</span></h1>
      <dl class="contact">
        <dt class="contact__label">Phone</dt>
        <dd class="contact__value">+1 310 555 0142</dd>
        <dt class="contact__label">Email</dt>
        <dd class="contact__value">norahale@mailbox.net</dd>
        <dt class="contact__label">Address</dt>
        <dd class="contact__value">218 Harbor Lane</dd>
        <dt class="contact__label"></dt>
        <dd class="contact__value">Ocean Park</dd>
        <dt class="contact__label"></dt>
        <dd class="contact__value">90411 CA USA</dd>
      </dl>
    </section>
    <section class="card card--back" aria-label="Business card back">
      <p class="name">Nora <span class="name__last">Hale</span></p>
    </section>
  </main>
</body>
</html>
```